Construction Business Card Design

We have a landscape construction company based in Australia
Were out of business cards ,
So now we're after a fresh looking modern card to give a fresh look to our business ....
We would like the business card to have the
(Front)
Tallow Ridge Pty Ltd
Director Norman Cusk
0462395108
(Back)
Landscape,Construction,Paving,Excavation
(In smaller font low in the frame of card)
Different textures , curved edge , vertical and horizontal designs also minimal colours per design
Eg one side black , one coloured or a splash here or there
Industry/Entity Type
Landscape
Contact Information for Business Card
Tallow Ridge Pty Ltd
Director Norman Cusk
0462395108
Landscape,Paving,Construction,Excavation
Look and feel

```html
<!DOCTYPE html>
<html lang="en">
<head>
<meta charset="utf-8">
<title>Tallow Ridge Pty Ltd — Business Card</title>
<link rel="stylesheet" href="https://fonts.googleapis.com/css2?family=Open+Sans:wght@700&family=Crimson+Text:ital@1&display=swap">
<style>
  :root {
    --page: #ffffff;
    --card: #1e1e1e;
    --band-gold: #f9d46a;
    --band-gold-deep: #e8bd4f;
    --text-light: #f2f2f2;
    --text-soft: #e4e4e4;
    --shadow: rgba(0, 0, 0, 0.45);
  }
  * { margin: 0; padding: 0; box-sizing: border-box; }
  html, body {
    width: 1200px;
    height: 960px;
    overflow: hidden;
    background: var(--page);
  }
  .canvas {
    position: relative;
    width: 1200px;
    height: 960px;
  }
  .business-card {
    position: absolute;
    left: 248px;
    top: 259px;
    width: 672px;
    height: 413px;
    background: var(--card);
    box-shadow: 8px 8px 8px var(--shadow);
    overflow: hidden;
  }
  .accent-band {
    position: absolute;
    left: 0;
    top: 0;
    width: 80px;
    height: 100%;
    background: linear-gradient(180deg, var(--band-gold), var(--band-gold-deep));
  }
  .identity {
    position: absolute;
    right: 64px;
    top: 62px;
    text-align: right;
  }
  .company {
    display: flex;
    align-items: center;
    justify-content: flex-end;
    gap: 16px;
    font-family: "Open Sans", sans-serif;
    font-weight: 700;
    font-size: 29px;
    color: var(--text-light);
    line-height: 1;
  }
  .company-mark {
    width: 40px;
    height: 40px;
    background: var(--band-gold);
  }
  .director {
    margin-top: 8px;
    font-family: "Crimson Text", serif;
    font-style: italic;
    font-size: 33px;
    color: var(--text-soft);
    line-height: 1.1;
  }
  .phone {
    margin-top: 2px;
    font-family: "Crimson Text", serif;
    font-style: italic;
    font-size: 31px;
    letter-spacing: 1.5px;
    color: var(--text-soft);
    line-height: 1.1;
  }
  .services {
    position: absolute;
    right: 56px;
    bottom: 42px;
    font-family: "Crimson Text", serif;
    font-style: italic;
    font-size: 32px;
    letter-spacing: 0.3px;
    color: var(--text-soft);
    white-space: nowrap;
  }
</style>
</head>
<body>
  <main class="canvas">
    <article class="business-card">
      <div class="accent-band" role="img" aria-label="Yellow and black diagonal safety stripe band"></div>
      <header class="identity">
        <h1 class="company"><span class="company-mark"></span>TALLOW RIDGE Pty Ltd</h1>
        <p class="director">Director : Norman Cusk</p>
        <p class="phone">0462395108</p>
      </header>
      <p class="services">Landscape,Construction,Paving,Excavation</p>
    </article>
  </main>
</body>
</html>
```